theater production in Seoul needs a poster of "Courtship Tutor: The Revue"

Title: "Courtship Tutor: The Revue"
Concept: This is a lively and fun musical centered around a dating coach who helps people navigate the ups and downs of modern romance. The show is full of humor, love, and the occasional heartache, highlighting the challenges of finding true love in today's world.
Visual Style: We are aiming for a vibrant and eye-catching design that captures the playful and romantic mood of the show. Think of bright colors, romantic symbols like hearts or arrows, and a modern urban setting. It should feel inviting, slightly humorous, and engaging.
Target Audience: Young adults and adults who enjoy romantic comedies and upbeat musicals. The tone should be fun and light, with a hint of romance.
Key Imagery: Possible elements could include a charismatic coach character holding a notepad or a whistle, silhouettes of couples, a city skyline in the background, or playful icons like phones, roses, and hearts. We want the poster to convey a sense of romance, excitement, and fun.

Text Elements:

Catchy tagline: "Finding love, one date at a time!"

Performance dates:2025. March 15_ May 31th
Sat. 1PM, Sun. 3pm, Wed/Fri 7:30pm

where:Hwasolgil Arthall
TICKET PRICE: $45
on the bottom side
Author Pyo Dain
Director-Gil Sorahm Composer_Moonbitnari
Producer_Ryu Donghwan Sound Director _Ahn Wol
actor_Tak Minjae Jeon Hyerin Nam Jiwoon Ha Boram Yeo Sanghun Cha Dohyeon

BOOK NOW
02 418-3956
PLUM COMPANY

```html
<!DOCTYPE html>
<html lang="en">
<head>
<meta charset="utf-8">
<title>Courtship Tutor: The Revue</title>
<link href="https://fonts.googleapis.com/css2?family=Allura&family=Poppins:ital,wght@0,400;0,600;0,700;1,700&display=swap" rel="stylesheet">
<style>
  :root{
    --backdrop:#9a9a9a;
    --poster-red:#c11f30;
    --band-red:#cf3b42;
    --heart-peach:#e0897a;
    --heart-deep:#9e1b2b;
    --heart-mid:#b4283a;
    --ink-white:#ffffff;
    --badge-black:#050505;
    --script:"Allura", cursive;
    --sans:"Poppins", sans-serif;
  }
  *{margin:0;padding:0;box-sizing:border-box;}
  html,body{width:1200px;height:1200px;overflow:hidden;background:var(--backdrop);}
  .poster{
    position:absolute;left:240px;top:59px;width:722px;height:1083px;
    background:var(--poster-red);overflow:hidden;color:var(--ink-white);
    font-family:var(--sans);
  }
  .poster-art{position:absolute;inset:0;}
  .title{position:absolute;left:0;top:175px;width:722px;}
  .title-line{position:absolute;white-space:nowrap;line-height:1;transform:translateX(-50%);}
  .title-line--one{left:322px;top:0;}
  .title-line--two{left:405px;top:68px;}
  .script{font-family:var(--script);font-weight:400;font-size:84px;}
  .sans{font-family:var(--sans);font-weight:400;font-size:50px;}
  .book-badge{position:absolute;left:520px;top:498px;width:130px;height:130px;border-radius:50%;
    background:var(--badge-black);display:flex;align-items:center;justify-content:center;text-align:center;
    font-weight:700;font-size:22px;line-height:1.2;box-shadow:0 4px 6px rgba(0,0,0,.35);}
  .contact{position:absolute;left:492px;top:645px;width:182px;text-align:center;color:var(--poster-red);
    font-size:19px;line-height:1.3;}
  .contact-phone{font-weight:600;}
  .tagline{position:absolute;left:58px;top:680px;font-size:34px;line-height:1.2;}
  .tagline .love{font-family:var(--script);font-size:62px;line-height:.6;}
  .details{position:absolute;left:58px;top:812px;font-size:16px;line-height:1.3;}
  .details sup{font-size:9px;}
  .location{position:absolute;left:58px;top:869px;font-size:16px;}
  .location b{font-weight:700;font-style:italic;}
  .ticket{position:absolute;left:0;width:722px;top:932px;text-align:center;font-weight:600;font-size:22px;}
  .credits{position:absolute;left:0;width:722px;top:975px;text-align:center;font-size:11.5px;line-height:1.33;}
</style>
</head>
<body>
<main class="poster">
  <svg class="poster-art" width="722" height="1083" viewBox="0 0 722 1083">
    <defs>
      <linearGradient id="heartFill" x1="0" y1="0" x2="0" y2="1">
        <stop offset="0" stop-color="var(--heart-deep)"/>
        <stop offset="0.6" stop-color="var(--heart-mid)"/>
        <stop offset="1" stop-color="#c8584f"/>
      </linearGradient>
    </defs>
    <path class="brush-band" fill="var(--band-red)" d="M0,1000 C150,960 300,930 420,910 C520,880 620,870 722,840 L722,950 C600,990 420,1030 250,1060 L0,1083Z"/>
    <path class="heart-frame" fill="var(--heart-peach)" d="M361,700 C240,600 0,480 5,265 C10,115 130,50 225,62 C295,70 335,115 352,160 C380,95 455,42 565,52 C690,62 740,165 722,290 C705,450 480,590 361,700Z"/>
    <path class="heart-photo" role="img" aria-label="Photo of a smiling couple sitting together, one playing a guitar, tinted red" fill="url(#heartFill)" d="M360,640 C260,560 55,460 58,275 C62,150 150,100 225,108 C285,115 325,155 350,205 C378,140 445,95 555,102 C660,110 690,190 680,290 C665,430 470,550 360,640Z"/>
    <circle class="contact-ring" cx="583" cy="669" r="100" fill="none" stroke="var(--ink-white)" stroke-width="3"/>
    <circle class="contact-disc" cx="583" cy="669" r="93" fill="var(--ink-white)" stroke="var(--poster-red)" stroke-width="3"/>
  </svg>

  <h1 class="title">
    <span class="title-line title-line--one"><span class="script">Courtship</span> <span class="sans">Tutor</span></span>
    <span class="title-line title-line--two"><span class="sans">The</span> <span class="script">Revue</span></span>
  </h1>

  <div class="book-badge">BOOK<br>NOW</div>
  <p class="contact"><span class="contact-phone">02 418-3956</span><br>PLUM COMPANY</p>

  <p class="tagline">Finding <span class="love">love,</span><br>one date at a time!</p>

  <p class="details">Performance dates: 2025. March 15<sup>th</sup> - May 31<sup>st</sup><br>Sat. 1PM, Sun. 3pm, Wed/Fri 7:30pm</p>
  <p class="location"><b>Location:</b> Hwasolgil Arthall</p>

  <p class="ticket">TICKET PRICE: $45</p>
  <p class="credits">Author Pyo Dain<br>Director-Gil Sorahm Composer_Moonbitnari<br>Producer_Ryu Donghwan Sound Director _Ahn Wol<br>actor_Tak Minjae Jeon Hyerin Nam Jiwoon Ha Boram Yeo Sanghun Cha Dohyeon</p>
</main>
</body>
</html>
```